Oil and Gas Letterhead Design Tweak

Simple letterhead information and design tweak.

Please note, we don't want to change the design or logo of the letterhead only the small changes mentioned below.

We need to change the company name up top to "Northvale Petrotek FZCO"

Also, we need to include in the footer the following information. I have attached an image of roughly how we would like to have it displayed in the footer.

Footer Details:

Northvale Petrotek FZCO,
Unit No. 2378, FZCO Trade Hub, level No. 1, K&P 7, Dubai, United Arab Emirates
Northvale Petrotek FZCO is registered as a free zone company under the rules & regulations of FZCO

Target Market(s)

O&G Market

Industry/Entity Type

Oil And Gas

Font styles to use
Sans Serif

Colors

Designer to choose colors to be used in the design.

Requirements
Must have
• Change the company name to Northvale Petrotek FZCO
• Include the footer on the bottom of the first and continuation page
Should not have
• Should not change the design or logo of the letterhead, only the specified changes mentioned above

```html
<!DOCTYPE html>
<html lang="en">
<head>
<meta charset="utf-8">
<title>Northvale Petrotek FZCO – Letterhead Set</title>
<link rel="stylesheet" href="https://fonts.googleapis.com/css2?family=Lato:wght@400;700&display=swap">
<style>
  :root {
    --backdrop: #d9dbdf;
    --paper: #ffffff;
    --brand-blue: #1557a6;
    --brand-red: #e3232b;
    --ink: #231f20;
    --ink-soft: #3a3a3a;
  }
  html, body {
    margin: 0;
    padding: 0;
    width: 1200px;
    height: 1200px;
    overflow: hidden;
    background: var(--backdrop);
    font-family: "Lato", sans-serif;
  }
  .sheet {
    position: absolute;
    width: 396px;
    height: 560px;
    background: var(--paper);
  }
  .sheet--first { left: 186px; top: 20px; }
  .sheet--continuation { left: 617px; top: 20px; }
  .sheet--continuation-alt { left: 409px; top: 619px; }
  .sheet svg { display: block; width: 100%; height: 100%; }
  .band-blue { fill: var(--brand-blue); }
  .band-red { fill: var(--brand-red); }
  .company-name { font-family: "Lato", sans-serif; font-size: 19px; fill: var(--ink); letter-spacing: 0.6px; }
  .footer-title { font-family: "Lato", sans-serif; font-weight: 700; fill: var(--ink); }
  .footer-line { font-family: "Lato", sans-serif; font-weight: 400; fill: var(--ink-soft); }
  .sign-name { font-family: "Lato", sans-serif; font-size: 8px; fill: var(--ink); }
</style>
</head>
<body>

<!-- First page -->
<div class="sheet sheet--first">
  <svg viewBox="0 0 637 902" aria-label="First page letterhead">
    <polygon class="band-blue" points="0,0 128,0 122,12 0,12"/>
    <polygon class="band-red" points="180,0 637,0 637,12 186,12"/>
    <rect class="band-blue" x="150" y="47" width="16" height="16"/>
    <text class="company-name" x="182" y="62">NORTHVALE PETROTEK FZCO</text>

    <text class="footer-title" x="32" y="826" font-size="12.5">NORTHVALE PETROTEK FZCO</text>
    <text class="footer-line" x="32" y="849" font-size="12" textLength="570" lengthAdjust="spacing">Unit No. 2378   |   FZCO Trade Hub   |   level No. 1, K&amp;P 7   |   Dubai   |   United Arab Emirates</text>
    <text class="footer-line" x="32" y="869" font-size="11.4" textLength="568" lengthAdjust="spacing">Northvale Petrotek FZCO is registered as a free zone company under the rules &amp; regulations of FZCO</text>

    <polygon class="band-blue" points="462,902 467,890 494,890 489,902"/>
    <polygon class="band-red" points="495,902 500,890 522,890 527,902"/>
  </svg>
</div>

<!-- Continuation page -->
<div class="sheet sheet--continuation">
  <svg viewBox="0 0 637 902" aria-label="Continuation page letterhead">
    <polygon class="band-blue" points="467,0 519,0 511,18 475,18"/>
    <polygon class="band-red" points="522,0 566,0 556,18 512,18"/>

    <text class="footer-title" x="32" y="824" font-size="10.5">NORTHVALE PETROTEK FZCO</text>
    <text class="footer-line" x="32" y="843" font-size="9.6" textLength="472" lengthAdjust="spacing">Unit No. 2378   |   FZCO Trade Hub   |   level No. 1, K&amp;P 7   |   Dubai   |   United Arab Emirates</text>
    <text class="footer-line" x="32" y="860" font-size="9.2" textLength="470" lengthAdjust="spacing">Northvale Petrotek FZCO is registered as a free zone company under the rules &amp; regulations of FZCO</text>

    <rect class="band-blue" x="538" y="836" width="14" height="14"/>
    <text class="sign-name" x="545" y="868" text-anchor="middle">NORTHVALE</text>
    <text class="sign-name" x="545" y="877" text-anchor="middle">PETROTEK</text>
    <text class="sign-name" x="545" y="886" text-anchor="middle">FZCO</text>

    <polygon class="band-blue" points="0,890 502,890 497,902 0,902"/>
    <polygon class="band-red" points="588,882 637,882 637,902 600,902"/>
  </svg>
</div>

<!-- Continuation page, second variant -->
<div class="sheet sheet--continuation-alt">
  <svg viewBox="0 0 637 902" aria-label="Continuation page letterhead variant">
    <polygon class="band-blue" points="467,0 519,0 511,18 475,18"/>
    <polygon class="band-red" points="522,0 566,0 556,18 512,18"/>

    <text class="footer-title" x="32" y="824" font-size="10.5">NORTHVALE PETROTEK FZCO</text>
    <text class="footer-line" x="32" y="843" font-size="9.6" textLength="472" lengthAdjust="spacing">Unit No. 2378   |   FZCO Trade Hub   |   level No. 1, K&amp;P 7   |   Dubai   |   United Arab Emirates</text>
    <text class="footer-line" x="32" y="860" font-size="9.2" textLength="470" lengthAdjust="spacing">Northvale Petrotek FZCO is registered as a free zone company under the rules &amp; regulations of FZCO</text>

    <rect class="band-blue" x="538" y="836" width="14" height="14"/>
    <text class="sign-name" x="545" y="868" text-anchor="middle">NORTHVALE</text>
    <text class="sign-name" x="545" y="877" text-anchor="middle">PETROTEK</text>
    <text class="sign-name" x="545" y="886" text-anchor="middle">FZCO</text>

    <polygon class="band-blue" points="0,890 502,890 497,902 0,902"/>
    <polygon class="band-red" points="588,882 637,882 637,902 600,902"/>
  </svg>
</div>

</body>
</html>
```